Animal Eye Clinic needs a Business card

We are a new veterinary ophthalmology practice (Silverbrook Pet Vision Care) and we need a business card designed. We only see animal eyes - we are not a regular veterinary clinic. We already have a logo. We are looking for a professional, good looking business card to hand out to our clients. We are looking for something simple but professional and contemporary. Our logo is likely the only picture/graphic that needs to be on the card.

Contact Information for Business Card

Marisol Quent, BSc, DVM, MSc, DipACVO
Veterinary Ophthalmologist

Phone: 250.419.3067
Email: silverbrookpetvisioncare@mailvero.com
Website: silverbrookpetvisioncare.com
Address: 1875 Tessock Rd
Kelowna, BC, V4T 8M3

Colors

Designer to choose colors to be used in the design.

Requirements
Must have
• Our logo (attached)

```html
<!DOCTYPE html>
<html lang="en">
<head>
<meta charset="utf-8">
<title>Silverbrook Pet Vision Care – Business Card</title>
<link href="https://fonts.googleapis.com/css2?family=Roboto:wght@400;500;700&display=swap" rel="stylesheet">
<style>
  :root {
    --teal: #0899a9;
    --teal-dark: #067f8d;
    --grey: #6f6f6f;
    --grey-light: #8a8a8a;
    --paper: #ffffff;
    --backdrop: #e9ecee;
  }
  * { box-sizing: border-box; margin: 0; padding: 0; }
  html, body {
    width: 1200px; height: 913px; overflow: hidden;
    background: var(--backdrop);
    font-family: "Roboto", Arial, sans-serif;
  }
  .stage { position: relative; width: 1200px; height: 913px; }
  .card {
    position: absolute; width: 560px; height: 320px;
    border-radius: 18px; overflow: hidden;
    box-shadow: 0 10px 28px rgba(0,0,0,.18);
  }
  .card--front { left: 70px; top: 80px; background: var(--teal); }
  .card--back { left: 570px; top: 510px; background: var(--paper); }

  .brand { display: flex; align-items: center; gap: 12px; }
  .brand__dot { width: 44px; height: 44px; border-radius: 50%; flex: none; }
  .brand__name {
    font-weight: 700; text-transform: uppercase; line-height: 1.15;
    letter-spacing: .04em;
  }
  .card--front .brand {
    position: absolute; left: 50%; top: 50%; transform: translate(-50%, -50%);
  }
  .card--front .brand__dot { background: var(--paper); }
  .card--front .brand__name { color: var(--paper); font-size: 22px; }

  .card--back .brand { position: absolute; left: 30px; top: 36px; }
  .card--back .brand__dot { width: 36px; height: 36px; background: var(--teal); }
  .card--back .brand__name { color: var(--teal); font-size: 15px; }

  .illustration { position: absolute; right: 0; top: 0; width: 280px; height: 320px; }

  .person { position: absolute; left: 30px; top: 118px; }
  .person__marker {
    position: absolute; left: -30px; top: 4px; width: 0; height: 0;
    border-top: 9px solid transparent; border-bottom: 9px solid transparent;
    border-left: 12px solid var(--teal);
  }
  .person__name { color: var(--teal); font-size: 21px; font-weight: 700; letter-spacing: .02em; }
  .person__credentials { color: var(--teal); font-size: 13px; margin-top: 3px; }
  .person__title { color: var(--grey); font-size: 13px; margin-top: 2px; }

  .address { position: absolute; left: 30px; top: 198px; color: var(--grey); font-size: 13px; line-height: 1.4; }

  .contacts { position: absolute; left: 30px; top: 244px; list-style: none; color: var(--grey); font-size: 12.5px; }
  .contacts li { display: flex; align-items: center; gap: 6px; line-height: 1.45; }
  .contacts svg { width: 11px; height: 11px; fill: var(--teal); flex: none; }
</style>
</head>
<body>
<main class="stage">

  <section class="card card--front" aria-label="Card front">
    <div class="brand">
      <span class="brand__dot"></span>
      <span class="brand__name">Silverbrook<br>Pet Vision Care</span>
    </div>
  </section>

  <section class="card card--back" aria-label="Card back">
    <div class="brand">
      <span class="brand__dot"></span>
      <span class="brand__name">Silverbrook<br>Pet Vision Care</span>
    </div>

    <svg class="illustration" viewBox="0 0 280 320" role="img" aria-label="Large illustration of horse, dog and cat heads in teal and grey">
      <defs>
        <linearGradient id="illustration-fill" x1="0" y1="0" x2="0.3" y2="1">
          <stop offset="0" stop-color="#0899a9"/>
          <stop offset="0.7" stop-color="#0899a9"/>
          <stop offset="1" stop-color="#7a7a7a"/>
        </linearGradient>
      </defs>
      <path d="M0 62 C60 40 150 30 210 40 C260 60 285 110 280 160 L280 250 C250 280 190 290 150 285 L90 300 C70 290 60 250 50 200 C40 140 30 90 0 62 Z" fill="url(#illustration-fill)"/>
    </svg>

    <div class="person">
      <span class="person__marker"></span>
      <h1 class="person__name">MARISOL QUENT</h1>
      <p class="person__credentials">BSc, DVM, MSc, DipACVO</p>
      <p class="person__title">Veterinary Ophthalmologist</p>
    </div>

    <address class="address" style="font-style:normal">
      1875 Tessock Rd<br>Kelowna, BC, V4T 8M3
    </address>

    <ul class="contacts">
      <li>
        <svg viewBox="0 0 24 24"><path d="M6.6 10.8a15.1 15.1 0 0 0 6.6 6.6l2.2-2.2c.3-.3.7-.4 1-.2 1.1.4 2.3.6 3.6.6.6 0 1 .4 1 1V20c0 .6-.4 1-1 1A17 17 0 0 1 3 4c0-.6.4-1 1-1h3.5c.6 0 1 .4 1 1 0 1.3.2 2.5.6 3.6.1.3 0 .7-.2 1z"/></svg>
        250.419.3067
      </li>
      <li>
        <svg viewBox="0 0 24 24"><path d="M2 5h20v14H2z M2 5l10 8 10-8" /></svg>
        silverbrookpetvisioncare@mailvero.com
      </li>
      <li>
        <svg viewBox="0 0 24 24"><circle cx="12" cy="12" r="10"/></svg>
        silverbrookpetvisioncare.com
      </li>
    </ul>
  </section>

</main>
</body>
</html>
```